Celling poster

It is a celling poster with questions that you ask yourself in the morning and a morning prayer + evening questions. People might put it on celling or on the wall.

Here is the contant, it is in Slovenian, but I have send you translation.

PO JUTRU SE DAN POZNA ...

1. Kaj me trenutno najbolj veseli v življenju?
3. Na kaj sem ponosna v življenju?
4. Za katere stvari danes čutim največ hvaležnosti?
5. V čem trenutno najbolj uživam?
6. Koga imam rada in kdo me ima rad?

Danes vstajam
s pomočjo nebeških sil:
svetlobe sonca,
sija lune,
žara ognja,
hitrosti strele,
okretnosti vetra,
globine morja,
stanovitnosti zemlje,
trdnosti skale.

VEČERNE MODROSTI

1. Kaj je bil danes moj prispevek svetu?
2. Kaj sem se danes naučila?
3. Katera situacija v dnevu mi je prinesla največ občutkov topline?

TRANSLATION for your understanding.

MORNING POWER QUESTIONS
1. What am I happy abou in my life right now?
2. What am I excited about in my life now?
3. What am I proud about in my life now?
4. What am I grateful about in my life now?
5. What am I enjoying most in my life now?
6. Who do I love? Who loves me?

MORNING PRAYER
Today I am waking up with the power of heavenly forces.
With the light of sun,
light of moon,
light of fire,
speed of lightning,
flexibility of wind,
depps of ocean,
stability of earth and
hardness of rock.

EVENING QUESTIONS OF WISDOM
1. What have I given today?
2. What did I learn today?
3. Which situations today gave me the most feelings of love, warmth?

```html
<!DOCTYPE html>
<html lang="sl">
<head>
<meta charset="UTF-8">
<title>Po jutru se dan pozna</title>
<link rel="stylesheet" href="https://fonts.googleapis.com/css2?family=Righteous&family=Roboto:wght@700&family=Dancing+Script:wght@500;700&display=swap">
<style>
  :root {
    --sky-top: #f27424;
    --sky-orange: #f79a1c;
    --sky-gold: #fcc21f;
    --haze: #fff6d6;
    --mist-blue: #4ea6d2;
    --cloud: #eaf2f6;
    --dusk: #3f5a86;
    --night: #101636;
    --night-deep: #0a0d27;
    --ink: #0f0f22;
    --white: #ffffff;
    --sun-disc: rgba(255, 240, 190, 0.55);
  }
  * { margin: 0; padding: 0; box-sizing: border-box; }
  html, body { width: 900px; height: 1200px; overflow: hidden; background: var(--night-deep); }
  .poster {
    position: relative;
    width: 900px;
    height: 1200px;
    overflow: hidden;
    font-family: "Roboto", Arial, sans-serif;
  }
  .sky-scene {
    position: absolute; inset: 0;
    background:
      radial-gradient(circle at 700px 480px, rgba(255, 226, 20, 0.75) 0, rgba(255, 220, 40, 0.35) 90px, rgba(255, 210, 60, 0) 220px),
      radial-gradient(ellipse 520px 110px at 700px 760px, rgba(255,255,255,0.55), rgba(255,255,255,0)),
      radial-gradient(ellipse 600px 90px at 250px 860px, rgba(255,255,255,0.45), rgba(255,255,255,0)),
      radial-gradient(ellipse 700px 80px at 620px 990px, rgba(220,230,240,0.35), rgba(220,230,240,0)),
      linear-gradient(180deg,
        var(--sky-top) 0%,
        var(--sky-orange) 28%,
        var(--sky-gold) 44%,
        #fde58a 52%,
        var(--haze) 60%,
        #d6ecf3 66%,
        var(--mist-blue) 71%,
        #9fcbe3 75%,
        var(--cloud) 79%,
        #8fa6c2 84%,
        var(--dusk) 88%,
        var(--night) 93%,
        var(--night-deep) 100%);
  }
  .sun-disc {
    position: absolute;
    left: 270px; top: 404px;
    width: 344px; height: 344px;
    border-radius: 50%;
    background: var(--sun-disc);
  }
  .heading {
    position: absolute;
    font-family: "Righteous", "Arial Black", sans-serif;
    font-weight: 400;
    line-height: 1;
    white-space: nowrap;
  }
  .heading--morning { left: 74px; top: 72px; font-size: 50px; color: var(--ink); }
  .heading--prayer  { left: 0; width: 900px; top: 350px; font-size: 60px; color: var(--ink); text-align: center; text-indent: 10px; }
  .heading--evening { left: 70px; top: 932px; font-size: 54px; color: var(--white); }
  .question-list {
    position: absolute;
    list-style: none;
    font-weight: 700;
    font-size: 21px;
    white-space: nowrap;
  }
  .question-list--morning { left: 76px; top: 136px; color: var(--ink); line-height: 29.7px; }
  .question-list--evening { left: 72px; top: 1014px; color: var(--white); line-height: 40px; }
  .prayer {
    position: absolute;
    left: 0; top: 438px; width: 890px;
    text-align: center;
    font-family: "Dancing Script", cursive;
    color: var(--ink);
  }
  .prayer__intro { font-size: 34px; font-weight: 700; line-height: 48px; }
  .prayer__forces { list-style: none; font-size: 30px; font-weight: 500; line-height: 42.2px; margin-top: 4px; }
</style>
</head>
<body>
<main class="poster">
  <div class="sky-scene" role="img" aria-label="Sunrise sky in orange and gold above misty blue mountains and clouds fading into a dark night sky"></div>
  <div class="sun-disc"></div>

  <h1 class="heading heading--morning">PO JUTRU SE DAN POZNA ...</h1>
  <ol class="question-list question-list--morning">
    <li>1. Kaj me trenutno najbolj veseli v življenju?</li>
    <li>3. Na kaj sem ponosna v življenju?</li>
    <li>4. Za katere stvari danes čutim največ hvaležnosti?</li>
    <li>5. V čem trenutno najbolj uživam?</li>
    <li>6. Koga imam rada in kdo me ima rad?</li>
  </ol>

  <h2 class="heading heading--prayer">Danes vstajam</h2>
  <div class="prayer">
    <p class="prayer__intro">s pomočjo<br>nebeških sil:</p>
    <ul class="prayer__forces">
      <li>svetlobe sonca,</li>
      <li>sija lune,</li>
      <li>žara ognja,</li>
      <li>hitrosti strele,</li>
      <li>okretnosti vetra,</li>
      <li>globine morja,</li>
      <li>stanovitnosti zemlje,</li>
      <li>trdnosti skale.</li>
    </ul>
  </div>

  <h2 class="heading heading--evening">VEČERNE MODROSTI</h2>
  <ol class="question-list question-list--evening">
    <li>1. Kaj je bil danes moj prispevek svetu?</li>
    <li>2. Kaj sem se danes naučila?</li>
    <li>3. Katera situacija v dnevu mi je prinesla največ občutkov topline?</li>
  </ol>
</main>
</body>
</html>
```